The Circle BOLQ: Global Policy to Local Action

We need two professional visuals that represent the vision and strategy of the organization. I attached two rough images of the first visual and one image of the second visual. I also attached a pdf of the narrative to give context for each visual.

Target Market(s)

Global Health Policy Makers

Colors
ec1f27

Requirements
Must have
• Two separate images representing the flow of the work

```html
<!DOCTYPE html>
<html lang="en">
<head>
<meta charset="utf-8">
<title>The Circle BOLQ – Global Policy to Local Action</title>
<link href="https://fonts.googleapis.com/css2?family=Roboto+Condensed:wght@400;700&display=swap" rel="stylesheet">
<style>
  :root {
    --red: #ec1f27;
    --red-deep: #d21f2b;
    --red-soft: #dc3e4a;
    --pink: #e27a80;
    --pink-wash: #f6d2d5;
    --purple: #5b2c83;
    --ink: #3b3b3d;
    --text: #3f3f41;
    --stage: #58595b;
    --ring-grey: #e3e3e4;
    --paper: #ffffff;
  }
  html, body {
    margin: 0;
    padding: 0;
    width: 1200px;
    height: 456px;
    overflow: hidden;
    background: var(--stage);
    font-family: "Roboto Condensed", "Arial Narrow", sans-serif;
  }
  .slide {
    position: absolute;
    top: 43px;
    width: 521px;
    height: 368px;
    background: var(--paper);
    box-shadow: 0 6px 14px rgba(0,0,0,.35);
  }
  .slide--partners { left: 63px; }
  .slide--network { left: 616px; }
  .slide svg { display: block; width: 100%; height: 100%; }
  .title { font-weight: 700; font-size: 36px; fill: var(--ink); }
  .title .accent { fill: var(--red); }
  .seg-label { font-size: 11px; fill: #fff; text-anchor: middle; }
  .hub-text { font-size: 11.5px; fill: var(--text); text-anchor: middle; }
  .brand { font-size: 17px; fill: var(--ink); letter-spacing: .6px; text-anchor: middle; }
  .goal-head { font-size: 10px; font-weight: 700; fill: var(--red); }
  .goal-item { font-size: 10px; fill: var(--text); }
  .tick { fill: none; stroke: var(--red); stroke-width: 1.3; }
  .icon { fill: none; stroke: var(--red); stroke-width: 1.4; stroke-linecap: round; stroke-linejoin: round; }
  .icon-ring { fill: #fff; stroke: var(--ink); stroke-width: 1.4; }
  .dash { fill: none; stroke: var(--ink); stroke-width: 1.4; stroke-dasharray: 5 4; }
  .dot { fill: var(--purple); }
  .band-text { font-size: 20px; font-weight: 700; fill: #fff; text-anchor: middle; }
  .header-text { font-size: 24px; font-weight: 700; fill: #fff; text-anchor: middle; }
  .arc-label { font-size: 11px; font-weight: 700; fill: var(--purple); }
  .node-label { font-size: 10px; font-weight: 700; fill: var(--red); }
</style>
</head>
<body>

<section class="slide slide--partners">
  <svg viewBox="0 0 842 595" aria-label="The partner diagram">
    <text class="title" x="421" y="100" text-anchor="middle">THE PARTNER <tspan class="accent">DIAGRAM</tspan></text>

    <g class="partner-wheel">
      <circle cx="252" cy="319" r="122.5" fill="none" stroke="var(--red-deep)" stroke-width="75"/>
      <circle cx="252" cy="319" r="122.5" fill="none" stroke="var(--red-soft)" stroke-width="75"
              stroke-dasharray="76.97 76.97" transform="rotate(-72 252 319)"/>
      <g stroke="#fff" stroke-width="2">
        <line x1="202.6" y1="166.8" x2="225.7" y2="238.2"/>
        <line x1="301.4" y1="166.8" x2="278.3" y2="238.2"/>
        <line x1="381.4" y1="224.9" x2="320.8" y2="269"/>
        <line x1="412" y1="319" x2="337" y2="319"/>
        <line x1="381.4" y1="413.1" x2="320.8" y2="369"/>
        <line x1="301.4" y1="471.2" x2="278.3" y2="399.8"/>
        <line x1="202.6" y1="471.2" x2="225.7" y2="399.8"/>
        <line x1="122.6" y1="413.1" x2="183.2" y2="369"/>
        <line x1="92" y1="319" x2="167" y2="319"/>
        <line x1="122.6" y1="224.9" x2="183.2" y2="269"/>
      </g>
      <circle cx="252" cy="319" r="85" fill="#fff"/>

      <text class="seg-label" x="252" y="189">Policy<tspan x="252" dy="14">Making</tspan></text>
      <text class="seg-label" x="327" y="202" font-size="10">Health,<tspan x="327" dy="13">Education &amp;</tspan><tspan x="327" dy="13">Labor Policy</tspan></text>
      <text class="seg-label" x="373" y="274">Education<tspan x="373" dy="14">&amp; Research</tspan></text>
      <text class="seg-label" x="373" y="340" font-size="10">Social &amp;<tspan x="373" dy="13">Professional</tspan><tspan x="373" dy="13">Networks</tspan></text>
      <text class="seg-label" x="323" y="411">Health<tspan x="323" dy="14">Workforce</tspan></text>
      <text class="seg-label" x="254" y="434" font-size="10">Community<tspan x="254" dy="13">Organization</tspan><tspan x="254" dy="13">&amp; Ownership</tspan></text>
      <text class="seg-label" x="180" y="416">Community</text>
      <text class="seg-label" x="131" y="335" font-size="10">Social<tspan x="131" dy="13">Institutions</tspan><tspan x="131" dy="13">&amp; Business</tspan><tspan x="131" dy="13">Leadership</tspan></text>
      <text class="seg-label" x="130" y="284">Management</text>
      <text class="seg-label" x="174" y="209" font-size="10">Political<tspan x="174" dy="13">Leadership</tspan></text>

      <text class="brand" x="252" y="318">THE CIRCLE BOLQ</text>
      <text class="hub-text" x="252" y="357">Health System based on<tspan x="252" dy="14">People’s Needs</tspan></text>
    </g>

    <circle cx="564" cy="300" r="104" fill="var(--pink-wash)" opacity=".8"/>
    <path class="dash" d="M252 130 A185 185 0 0 1 252 500"/>
    <circle class="dot" cx="252" cy="130" r="5"/>
    <circle class="dot" cx="252" cy="500" r="5"/>
    <g class="dash">
      <line x1="368" y1="171" x2="488" y2="171"/>
      <line x1="422" y1="243" x2="488" y2="243"/>
      <line x1="437" y1="314" x2="488" y2="314"/>
      <line x1="422" y1="388" x2="488" y2="388"/>
      <line x1="369" y1="458" x2="488" y2="458"/>
    </g>

    <g class="goal-icons">
      <circle class="icon-ring" cx="516" cy="171" r="28"/>
      <polyline class="icon" points="502,183 510,171 517,176 527,162"/>
      <line class="icon" x1="500" y1="185" x2="532" y2="185"/>
      <circle class="icon-ring" cx="516" cy="243" r="28"/>
      <circle class="icon" cx="508" cy="236" r="3.5"/><circle class="icon" cx="516" cy="233" r="3.5"/><circle class="icon" cx="524" cy="236" r="3.5"/>
      <path class="icon" d="M504 256 v-12 h8 v12 M512 256 v-16 h8 v16 M520 256 v-12 h8 v12"/>
      <circle class="icon-ring" cx="516" cy="314" r="28"/>
      <circle class="icon" cx="516" cy="311" r="9"/><circle class="icon" cx="516" cy="311" r="3.5"/>
      <circle class="icon-ring" cx="516" cy="388" r="28"/>
      <path class="icon" d="M508 404 L516 372 L524 404 M510 382 h12 M511 392 h10 M510 382 L522 392 M522 382 L510 392"/>
      <circle class="icon-ring" cx="516" cy="458" r="28"/>
      <path class="icon" d="M503 462 C505 448 520 446 526 450 C524 462 510 468 503 462 Z M503 462 L520 452"/>
      <g class="dot"><circle cx="489" cy="171" r="4.5"/><circle cx="489" cy="243" r="4.5"/><circle cx="489" cy="314" r="4.5"/><circle cx="489" cy="388" r="4.5"/><circle cx="489" cy="458" r="4.5"/></g>
    </g>

    <g class="goal-lists">
      <text class="goal-head" x="575" y="151">Economy</text>
      <text class="goal-item" x="575" y="166">Decent Work</text>
      <text class="goal-item" x="575" y="180">Adequate Income</text>
      <text class="goal-item" x="575" y="194">Quality Education &amp; Lifelong Learning</text>
      <text class="goal-head" x="575" y="230">Society</text>
      <text class="goal-item" x="575" y="247">Gender Equality</text>
      <text class="goal-item" x="575" y="261">Recreational Opportunities</text>
      <text class="goal-head" x="575" y="309">People</text>
      <text class="goal-item" x="575" y="325">Resilent Community</text>
      <text class="goal-head" x="575" y="373">Infrastructure</text>
      <text class="goal-item" x="575" y="390">Transportation for Accessibility</text>
      <text class="goal-item" x="575" y="405">Affordable &amp; Safe Housing</text>
      <text class="goal-head" x="575" y="438">Environment</text>
      <text class="goal-item" x="575" y="455">Affordable Clean Energy</text>
      <text class="goal-item" x="575" y="470">Availability of Healthy Food</text>
      <text class="goal-item" x="575" y="485">Clean Water &amp; Sanitation</text>
      <g class="tick">
        <path d="M562 162 l2.5 3 l5 -6"/><path d="M562 176 l2.5 3 l5 -6"/><path d="M562 190 l2.5 3 l5 -6"/>
        <path d="M562 243 l2.5 3 l5 -6"/><path d="M562 257 l2.5 3 l5 -6"/>
        <path d="M562 321 l2.5 3 l5 -6"/>
        <path d="M562 386 l2.5 3 l5 -6"/><path d="M562 401 l2.5 3 l5 -6"/>
        <path d="M562 451 l2.5 3 l5 -6"/><path d="M562 466 l2.5 3 l5 -6"/><path d="M562 481 l2.5 3 l5 -6"/>
      </g>
    </g>

    <rect x="0" y="544" width="842" height="51" fill="var(--red-deep)"/>
    <text class="band-text" x="421" y="577">Substainable Development Goals</text>
  </svg>
</section>

<section class="slide slide--network">
  <svg viewBox="0 0 842 595" aria-label="Global and regional partnerships">
    <defs>
      <linearGradient id="mapTone" x1="0" y1="0" x2="1" y2="1">
        <stop offset="0" stop-color="#cfd0d2"/>
        <stop offset="1" stop-color="#e6e7e8"/>
      </linearGradient>
      <path id="upperArc" d="M244 330 A173 173 0 0 1 590 330"/>
      <path id="lowerArc" d="M233 330 A184 184 0 0 0 601 330"/>
    </defs>

    <rect x="0" y="0" width="842" height="85" fill="var(--red-deep)"/>
    <text class="header-text" x="421" y="56">BOLQ drives is work through Global and Regional Partnerships</text>

    <g role="img" aria-label="World map in soft grey behind the network wheel">
      <rect x="55" y="160" width="740" height="370" rx="70" fill="url(#mapTone)" opacity=".7"/>
    </g>

    <circle cx="417" cy="330" r="225" fill="none" stroke="var(--ink)" stroke-width="1.4" stroke-dasharray="5 4"/>
    <circle cx="417" cy="330" r="180" fill="none" stroke="var(--ring-grey)" stroke-width="36" opacity=".95"/>

    <circle cx="417" cy="330" r="130" fill="none" stroke="var(--pink)" stroke-width="66"/>
    <circle cx="417" cy="330" r="130" fill="none" stroke="var(--red-deep)" stroke-width="66"
            stroke-dasharray="81.68 81.68" transform="rotate(-108 417 330)"/>
    <circle cx="417" cy="330" r="97" fill="#fff"/>

    <text class="arc-label"><textPath href="#upperArc" startOffset="17%" text-anchor="middle">Policy Papers</textPath></text>
    <text class="arc-label"><textPath href="#upperArc" startOffset="85%" text-anchor="middle">Publications</textPath></text>
    <text class="arc-label"><textPath href="#lowerArc" startOffset="50%" text-anchor="middle">Training Curricula</textPath></text>

    <text class="seg-label" x="417" y="199">Regional<tspan x="417" dy="14">Meetings</tspan></text>
    <text class="seg-label" x="535" y="296">Taskforces</text>
    <text class="seg-label" x="494" y="434">Conferences</text>
    <text class="seg-label" x="343" y="434">Symposiums</text>
    <text class="seg-label" x="296" y="297">Workshops</text>

    <text class="brand" x="417" y="332">THE CIRCLE BOLQ</text>
    <text class="hub-text" x="417" y="373" font-size="15">Network of Networks</text>

    <circle class="icon-ring" cx="192" cy="328" r="26"/>
    <circle class="icon" cx="192" cy="328" r="14"/>
    <ellipse class="icon" cx="192" cy="328" rx="6" ry="14"/>
    <path class="icon" d="M178 328 h28 M181 320 h22 M181 336 h22"/>
    <text class="node-label" x="158" y="333" text-anchor="end">GLOBAL POLICY</text>

    <circle class="icon-ring" cx="641" cy="326" r="26"/>
    <path class="icon" d="M641 341 C632 330 630 325 630 320 A11 11 0 0 1 652 320 C652 325 650 330 641 341 Z"/>
    <circle class="icon" cx="641" cy="320" r="4.5"/>
    <text class="node-label" x="675" y="333">LOCAL ACTION</text>

    <g class="info-blocks">
      <text class="goal-head" x="68" y="163">FRAMEWORKS</text>
      <text class="goal-item" x="68" y="182">Social Accountability &amp;</text>
      <text class="goal-item" x="68" y="195">Accreditation</text>
      <text class="goal-item" x="68" y="209">Interprofessional Education &amp;</text>
      <text class="goal-item" x="68" y="222">Team-based Care</text>
      <text class="goal-item" x="68" y="235">Population Health</text>
      <text class="goal-head" x="68" y="462">NETWORK KNOWLEDGE</text>
      <text class="goal-head" x="68" y="475">BEST PRACTICES</text>
      <text class="goal-item" x="68" y="495">Remote/Rural, Women, Migrants,</text>
      <text class="goal-item" x="68" y="509">Refugees, Indigenous Health</text>
      <text class="goal-head" x="657" y="163">GUIDING VALUES</text>
      <text class="goal-item" x="657" y="182">Community relevance</text>
      <text class="goal-item" x="657" y="196">Informed consumer</text>
      <text class="goal-item" x="657" y="209">Patient/Consumer voice</text>
      <text class="goal-item" x="657" y="222">Intersectoral, multi-disciplinary</text>
      <text class="goal-head" x="657" y="462">OUTCOME</text>
      <text class="goal-item" x="657" y="482">Coordinated Action by Local</text>
      <text class="goal-item" x="657" y="496">Change Agents and Networks</text>
      <g class="tick">
        <path d="M53 178 l2.5 3 l5 -6"/><path d="M53 205 l2.5 3 l5 -6"/><path d="M53 231 l2.5 3 l5 -6"/>
        <path d="M53 491 l2.5 3 l5 -6"/>
        <path d="M642 178 l2.5 3 l5 -6"/><path d="M642 192 l2.5 3 l5 -6"/><path d="M642 205 l2.5 3 l5 -6"/><path d="M642 218 l2.5 3 l5 -6"/>
        <path d="M642 478 l2.5 3 l5 -6"/>
      </g>
    </g>
  </svg>
</section>

</body>
</html>
```